Global Leadership Company requires banner design

I need 3 large banners designed. i will be using these for advertising and also a condensed version as the header on a splash pages.

I have attached the wording and also the photo's that i'd like used in each design.
Note: i've just placed the wording randomly, you'll have to place it where it makes the most sense for the message and the design.

I want something with bright colors that pops.

Reason: I'd like to give the most recent designers time to submit quality work.

```html
<!DOCTYPE html>
<html lang="en">
<head>
<meta charset="utf-8">
<title>Leadership Opportunity Banners</title>
<link rel="stylesheet" href="https://fonts.googleapis.com/css2?family=Oswald:wght@400;500;600;700&family=Courgette&display=swap">
<style>
  :root {
    --teal: #3d9dac;
    --teal-light: #5ec3d0;
    --orange: #f0a429;
    --green: #6dbb3a;
    --ink: #2e2e2e;
    --red: #c8161d;
    --red-dark: #9e0d12;
    --white: #ffffff;
  }
  * { margin: 0; padding: 0; box-sizing: border-box; }
  html, body { width: 1200px; height: 1126px; overflow: hidden; background: var(--white); }
  body { position: relative; font-family: "Oswald", sans-serif; color: var(--ink); }

  .banner { position: absolute; left: 0; width: 1200px; overflow: hidden; }
  .banner--wanted { top: 0; height: 359px; }
  .banner--passion { top: 376px; height: 356px; }
  .banner--tomorrow { top: 752px; height: 374px; }

  .banner__bg { position: absolute; inset: 0; width: 100%; height: 100%; }
  .abs { position: absolute; white-space: nowrap; }

  .headline { font-weight: 700; text-transform: uppercase; line-height: 1; }
  .script { font-family: "Courgette", cursive; color: var(--white); line-height: 1.1; text-shadow: 0 2px 3px rgba(0,0,0,.25); }
  .perks { font-weight: 600; font-style: italic; color: var(--red); text-transform: uppercase; line-height: 1.25; }
  .perks span { margin-right: 14px; }

  .cta {
    position: absolute; display: flex; align-items: center; justify-content: center;
    background: linear-gradient(#e8343a, var(--red) 55%, var(--red-dark));
    color: var(--white); font-weight: 600; text-transform: uppercase;
    border-radius: 20px; border: 2px solid var(--white);
    box-shadow: 0 3px 5px rgba(0,0,0,.35); letter-spacing: .3px;
  }

  .photo { position: absolute; border-radius: 50%; }

  /* Banner 1 */
  .wanted-word { left: 22px; top: 10px; font-size: 112px; color: var(--teal); letter-spacing: -1px; }
  .wanted-sub { left: 388px; top: 24px; font-size: 31px; line-height: 1.05; font-weight: 600; color: #3a3a3a; }
  .wanted-boom { left: 34px; top: 114px; font-size: 34px; font-weight: 600; color: #3a3a3a; }
  .wanted-quote { left: 48px; top: 184px; font-size: 31px; }
  .wanted-perks { left: 100px; top: 256px; font-size: 19px; }
  .wanted-launch { left: 34px; top: 316px; font-size: 29px; font-weight: 600; color: #3a3a3a; }
  .wanted-cta { left: 432px; top: 309px; width: 315px; height: 40px; font-size: 25px; }
  .testimonial { left: 698px; top: 280px; font-size: 15px; color: var(--white); font-style: italic; text-align: right; line-height: 1.25; }
  .testimonial b { display: block; font-family: "Courgette", cursive; font-weight: 400; font-size: 17px; margin-top: 4px; }
  .wanted-photo { left: 914px; top: -8px; width: 304px; height: 304px;
    background: radial-gradient(circle at 45% 40%, #e8c09a, #b98a5f 55%, #5b4a3a);
    border: 8px solid var(--white); box-shadow: 0 0 0 6px var(--teal-light); }

  /* Banner 2 */
  .passion-head { left: 34px; top: 20px; font-size: 35px; color: #222; }
  .passion-align { left: 346px; top: 62px; font-size: 27px; color: #222; }
  .passion-ready { left: 390px; top: 100px; font-size: 20px; color: #222; }
  .passion-quote { left: 336px; top: 176px; font-size: 32px; }
  .passion-perks { left: 364px; top: 276px; font-size: 20px; }
  .passion-cta { left: 702px; top: 312px; width: 322px; height: 38px; font-size: 25px; }
  .passion-photo { left: -6px; top: 68px; width: 300px; height: 300px;
    background: radial-gradient(circle at 50% 40%, #c99a74, #7a5a46 55%, #2b2a33);
    border: 8px solid var(--white); box-shadow: 0 0 0 6px var(--orange); }

  /* Banner 3 */
  .tomorrow-head { left: 380px; top: 26px; font-size: 49px; color: var(--red); }
  .tomorrow-learn { left: 380px; top: 94px; font-size: 27px; font-weight: 600; color: #222; }
  .tomorrow-hours { left: 380px; top: 133px; font-size: 23px; font-weight: 600; color: #222; }
  .tomorrow-quote { left: 436px; top: 190px; font-size: 42px; line-height: 1.05; }
  .tomorrow-perks { left: 430px; top: 290px; font-size: 21px; word-spacing: 2px; }
  .tomorrow-perks span { margin-right: 48px; }
  .tomorrow-cta { left: 590px; top: 322px; width: 306px; height: 42px; font-size: 26px; }
  .tomorrow-photo { left: -34px; top: 12px; width: 338px; height: 338px;
    background: radial-gradient(circle at 50% 42%, #d9a47c, #8a5c40 55%, #2a241f);
    border: 8px solid var(--white); box-shadow: 0 0 0 6px var(--green); }
</style>
</head>
<body>

<section class="banner banner--wanted">
  <svg class="banner__bg" viewBox="0 0 1200 359" preserveAspectRatio="none" aria-hidden="true">
    <defs>
      <linearGradient id="paperA" x1="0" y1="0" x2="0" y2="1">
        <stop offset="0" stop-color="#f7f7f7"/><stop offset="1" stop-color="#d8d8d8"/>
      </linearGradient>
      <linearGradient id="tealA" x1="0" y1="0" x2="0" y2="1">
        <stop offset="0" stop-color="#6fcad6"/><stop offset="1" stop-color="#3d9dac"/>
      </linearGradient>
    </defs>
    <rect width="1200" height="359" fill="url(#paperA)"/>
    <path d="M0 168 C300 150 700 110 1200 130 L1200 359 L0 359 Z" fill="#9fdbe3"/>
    <path d="M0 182 C320 166 720 130 1200 150 L1200 359 L0 359 Z" fill="url(#tealA)"/>
  </svg>
  <div class="abs headline wanted-word">Wanted</div>
  <div class="abs headline wanted-sub">Driven individuals ready to take<br>their results to the next level</div>
  <div class="abs headline wanted-boom">Personal Empowerment.....The Next Big Business Boom!</div>
  <div class="abs script wanted-quote">“Let us show you how we’ve taught average people to<br>earn an executives salary from home – part time. FAST!”</div>
  <div class="abs perks wanted-perks">
    <span>- Make up to $5,000 per sale</span><span>- No cold calling</span><br>
    <span>-No experience required</span><span>-No pressure selling</span><span>- Not MLM</span>
  </div>
  <div class="abs headline wanted-launch">Just launched in United States</div>
  <div class="cta wanted-cta">Click here for free info</div>
  <div class="abs testimonial">“Within just 5 months I was making<br>over $25,000 per month”<b>-Dana, Oregon</b></div>
  <div class="photo wanted-photo" role="img" aria-label="Portrait photo of a smiling blonde woman"></div>
</section>

<section class="banner banner--passion">
  <svg class="banner__bg" viewBox="0 0 1200 356" preserveAspectRatio="none" aria-hidden="true">
    <defs>
      <linearGradient id="paperB" x1="0" y1="0" x2="0" y2="1">
        <stop offset="0" stop-color="#f7f7f7"/><stop offset="1" stop-color="#dedede"/>
      </linearGradient>
      <linearGradient id="yellowB" x1="0" y1="0" x2="1" y2="0">
        <stop offset="0" stop-color="#f7c64a"/><stop offset="1" stop-color="#f0a429"/>
      </linearGradient>
    </defs>
    <rect width="1200" height="356" fill="url(#paperB)"/>
    <path d="M0 140 C400 200 800 110 1200 130 L1200 356 L0 356 Z" fill="#fbe19a"/>
    <path d="M0 156 C400 216 800 126 1200 146 L1200 356 L0 356 Z" fill="url(#yellowB)"/>
  </svg>
  <div class="photo passion-photo" role="img" aria-label="Photo of a couple in formal evening wear"></div>
  <div class="abs headline passion-head">Passionate about personal development / leadership development?</div>
  <div class="abs headline passion-align">Looking to align yourself with an opportunity of substance?</div>
  <div class="abs headline passion-ready">Ready to be challenged &amp; encouraged to reach new level’s of success?</div>
  <div class="abs script passion-quote">“Let us show you how we’ve taught others like you<br>to make a quantum leap in their personal results”</div>
  <div class="abs perks passion-perks">
    <span>- Make up to $5,000 per sale</span><span>- No cold calling</span><span>- No experience required</span><br>
    <span>- No pressure selling</span><span>- Not MLM</span>
  </div>
  <div class="cta passion-cta">Click here for free info</div>
</section>

<section class="banner banner--tomorrow">
  <svg class="banner__bg" viewBox="0 0 1200 374" preserveAspectRatio="none" aria-hidden="true">
    <defs>
      <linearGradient id="paperC" x1="0" y1="0" x2="0" y2="1">
        <stop offset="0" stop-color="#f7f7f7"/><stop offset="1" stop-color="#dedede"/>
      </linearGradient>
      <linearGradient id="greenC" x1="0" y1="0" x2="0" y2="1">
        <stop offset="0" stop-color="#9bd55a"/><stop offset="1" stop-color="#5fae2f"/>
      </linearGradient>
    </defs>
    <rect width="1200" height="374" fill="url(#paperC)"/>
    <path d="M0 210 C400 170 800 230 1200 170 L1200 374 L0 374 Z" fill="#c9eba2"/>
    <path d="M0 226 C400 186 800 246 1200 186 L1200 374 L0 374 Z" fill="url(#greenC)"/>
  </svg>
  <div class="photo tomorrow-photo" role="img" aria-label="Photo of a smiling couple posing together"></div>
  <div class="abs headline tomorrow-head">Change your tomorrow – Today!</div>
  <div class="abs headline tomorrow-learn">Learn to turn your spare time into an executive level income.</div>
  <div class="abs headline tomorrow-hours">In just 2 hours per day you can make a quantum leap in your results.</div>
  <div class="abs script tomorrow-quote">Learn our success formula today<br>&nbsp;so you can enjoy more tomorrow</div>
  <div class="abs perks tomorrow-perks"><span>More time</span><span>More fulfillment</span><span>More money</span><span>More fun</span></div>
  <div class="cta tomorrow-cta">Click here for free info</div>
</section>

</body>
</html>
```